Pop punk gig poster design!

In need of an amazing poster design for a gig We are organising, the genre is pop punk, and will be an all ages gig. I need to it bold, random and capture the eye of any bypasses, and make people want to go to the gig just because the poster is awesome! The event will be called "A glimpse of neon" and will consist of three bands and an acoustic set to open. All the bands are full of energy and create an unreal ambiance during there shows, I would like to capture that in the poster. Open to anything spectacular, the sky is the limit.

• I need to have the name of the event "A Glimpse Of Neon"
Band names(in this order):
-Fold the Lantern
-Velvet Orchard
-Gemwick's Oar
-Lunetta Pribble

Date: Saturday 10th November 2012
Time: 5:15pm
Venue: The Quill, 47 Marrowfen street, West End, QLD 4101
Ticket price: $10+bf online
$15 at the door.
Free BBQ

```html
<!DOCTYPE html>
<html lang="en">
<head>
<meta charset="utf-8">
<title>A Glimpse Of Neon — Gig Poster</title>
<link rel="stylesheet" href="https://fonts.googleapis.com/css2?family=Oswald:wght@300;600;700&family=Rubik+Dirt&family=Rubik+Wet+Paint&family=Share+Tech+Mono&display=swap">
<style>
  :root {
    --blood: #6e0d12;
    --blood-deep: #3a0508;
    --brush: #9b1117;
    --brush-dark: #7a0c11;
    --concrete: #2f2a2b;
    --title-pink: #d0646b;
    --ink: #0d0a0a;
    --band-grey: #5b5153;
    --date-ink: #221b1c;
    --ticket-text: #f0d6d8;
  }
  * { margin: 0; padding: 0; box-sizing: border-box; }
  html, body { width: 849px; height: 1200px; overflow: hidden; background: var(--ink); }
  .poster {
    position: relative;
    width: 849px;
    height: 1200px;
    overflow: hidden;
    background: var(--blood);
    font-family: "Oswald", sans-serif;
  }
  .backdrop { position: absolute; inset: 0; }
  .emblem-glow {
    position: absolute;
    left: 0; top: 0;
    width: 100px; height: 100px;
    border-radius: 50%;
    background: radial-gradient(circle, rgba(230,40,45,.55) 0%, rgba(160,20,25,.25) 50%, rgba(110,13,18,0) 72%);
  }
  .event-kicker {
    position: absolute;
    left: 205px; top: 16px;
    font-weight: 300;
    font-size: 54px;
    line-height: 1;
    letter-spacing: 28px;
    color: var(--ink);
    text-transform: uppercase;
    white-space: nowrap;
  }
  .event-title {
    position: absolute;
    left: 0; top: 80px;
    width: 849px;
    text-align: center;
    font-family: "Rubik Dirt", sans-serif;
    font-size: 170px;
    line-height: 1;
    letter-spacing: 8px;
    color: var(--title-pink);
    text-shadow: 6px 6px 0 var(--ink), 10px 12px 14px rgba(0,0,0,.6);
  }
  .title-strip {
    position: absolute;
    left: 6px; top: 151px;
    width: 820px; height: 22px;
    background: var(--brush-dark);
    border: 2px solid var(--ink);
    color: var(--ink);
    font-weight: 600;
    font-size: 17px;
    line-height: 18px;
    letter-spacing: 14px;
    text-align: center;
    white-space: nowrap;
  }
  .band {
    position: absolute;
    font-family: "Rubik Wet Paint", sans-serif;
    color: var(--band-grey);
    text-transform: uppercase;
    line-height: .9;
    white-space: nowrap;
    text-shadow: 3px 4px 0 var(--ink), 6px 8px 10px rgba(0,0,0,.7);
  }
  .band .lead { display: block; }
  .band .main { display: block; color: #4a4143; }
  .band--one { left: 130px; top: 395px; }
  .band--one .lead { font-size: 62px; padding-left: 12px; }
  .band--one .main { font-size: 84px; }
  .band--two { left: 440px; top: 560px; text-align: right; }
  .band--two .lead { font-size: 58px; }
  .band--two .main { font-size: 68px; }
  .band--three { left: 40px; top: 632px; }
  .band--three .lead { font-size: 50px; }
  .band--three .main { font-size: 86px; padding-left: 50px; }
  .band--four { left: 350px; top: 760px; transform: rotate(-6deg); }
  .band--four .lead { font-size: 54px; padding-left: 70px; }
  .band--four .main { font-size: 80px; }
  .ticket-heading {
    position: absolute;
    left: 95px; top: 805px;
    transform: rotate(6deg);
    font-family: "Rubik Wet Paint", sans-serif;
    font-size: 52px;
    line-height: .9;
    color: #4a4143;
    text-align: center;
    text-shadow: 3px 4px 0 var(--ink);
  }
  .ticket-prices {
    position: absolute;
    left: 22px; top: 862px;
    width: 150px;
    font-family: "Share Tech Mono", monospace;
    font-size: 22px;
    line-height: 1.1;
    color: var(--brush);
    text-align: center;
    text-transform: uppercase;
    -webkit-text-stroke: 1px var(--ticket-text);
  }
  .event-details {
    position: absolute;
    left: 55px; top: 1108px;
    transform: rotate(-15deg);
    transform-origin: left top;
    color: var(--date-ink);
    text-transform: uppercase;
    font-weight: 700;
    white-space: nowrap;
  }
  .event-date { font-size: 42px; letter-spacing: 5px; line-height: 1; }
  .event-venue { font-size: 21px; letter-spacing: 4px; line-height: 1.3; }
  .event-time {
    position: absolute;
    left: 330px; top: 1080px;
    transform: rotate(-10deg);
    font-size: 62px;
    font-weight: 700;
    letter-spacing: 4px;
    line-height: 1;
    color: var(--date-ink);
  }
  .event-extra {
    position: absolute;
    left: 630px; top: 1030px;
    width: 180px;
    text-align: center;
    font-size: 60px;
    font-weight: 700;
    letter-spacing: 6px;
    line-height: 1;
    color: var(--date-ink);
  }
</style>
</head>
<body>
<main class="poster">
  <svg class="backdrop" width="849" height="1200" viewBox="0 0 849 1200" aria-hidden="true">
    <defs>
      <radialGradient id="vignette" cx="50%" cy="40%" r="75%">
        <stop offset="65%" stop-color="#000" stop-opacity="0"/>
        <stop offset="100%" stop-color="#000" stop-opacity=".35"/>
      </radialGradient>
      <linearGradient id="topRed" x1="0" y1="0" x2="0" y2="1">
        <stop offset="0" stop-color="#7c1016"/>
        <stop offset="1" stop-color="#5a0a0e"/>
      </linearGradient>
    </defs>
    <rect class="sky" width="849" height="1200" fill="url(#topRed)"/>
    <polygon class="concrete-field" fill="#2f2a2b"
      points="0,290 40,270 70,300 110,265 150,310 200,280 260,320 320,285 370,315 430,280 480,310 540,275 600,300 660,270 720,305 780,280 849,300 849,860 0,1080"/>
    <g class="shards" fill="#4a0a0d">
      <polygon points="60,250 120,300 40,320"/>
      <polygon points="250,260 300,330 200,320"/>
      <polygon points="520,260 580,330 490,320"/>
      <polygon points="700,250 760,320 680,310"/>
    </g>
    <g class="brush-strokes" fill="#9b1117">
      <path d="M130,380 L470,370 L500,430 L460,500 L300,520 L180,515 L110,470 Z"/>
      <path d="M40,550 L520,540 L640,520 L849,530 L849,660 L620,640 L420,600 L200,610 L30,600 Z" fill="#8a0f14"/>
      <path d="M30,630 L330,620 L380,660 L360,740 L170,760 L20,730 Z"/>
      <path d="M380,690 L600,680 L760,720 L800,800 L700,850 L450,870 L370,830 Z" fill="#8a0f14"/>
      <path d="M90,790 L260,780 L290,860 L220,900 L100,890 Z" fill="#7a0c11"/>
    </g>
    <polygon class="date-band" fill="#8a0f15" points="0,1080 849,860 849,1200 0,1200"/>
    <rect width="849" height="1200" fill="url(#vignette)"/>
  </svg>

  <div class="emblem-glow" role="img" aria-label="Faint red circular emblem decoration"></div>

  <div class="event-kicker">Glimpse of</div>
  <h1 class="event-title">NEON</h1>
  <div class="title-strip">// A Glimpse of Neon //</div>

  <section class="lineup">
    <div class="band band--one"><span class="lead">Fold the</span><span class="main">Lantern</span></div>
    <div class="band band--two"><span class="lead">Velvet</span><span class="main">Orchard</span></div>
    <div class="band band--three"><span class="lead">Gemwick's</span><span class="main">Oar</span></div>
    <div class="band band--four"><span class="lead">Lunetta</span><span class="main">Pribble</span></div>
  </section>

  <div class="ticket-heading">Ticket<br>Price</div>
  <div class="ticket-prices">$10+bf<br>online<br>$15<br>at<br>the door</div>

  <div class="event-details">
    <p class="event-date">Saturday 10th November 2012</p>
    <p class="event-venue">The Quill, 47 Marrowfen Street, West End, QLD 4101</p>
  </div>
  <div class="event-time">5:15PM</div>
  <div class="event-extra">FREE<br>BBQ</div>
</main>
</body>
</html>
```